Rebranding Website – Brookvale Clinic for Herbal Care (40 Years)

Organization Description:
The Brookvale Clinic for Herbal Care (BCHC / www.bchc-example.nl) has been a trusted address for more than 40 years for people who choose a natural and sustainable approach to their health. We combine experience and history with a modern, professional approach.

Assignment:
Our current website is outdated and no longer reflects who we are today. We are looking for a new web design that aligns with our renewed logo and is both functional and inspiring. The website should have a clear structure, be user-friendly, and convey trust.

What we are looking for in the design:

A modern, fresh look that matches our logo and color palette logo in attachment.

Goal-oriented: simple and intuitive appointment scheduling.

Informative: space for a blog/news section to share knowledge and updates.

A dedicated page for each therapist with photo, expertise, and contact options.

A separate page for each type of therapy, with explanations and benefits.

A clear and visible link to our webshop (separate website).

Clear navigation and an organized menu structure.

Responsive design (desktop, tablet, mobile).

User-friendly CMS so we can manage and expand content ourselves.

Style Preferences:

- Color palette in line with our logo (green and natural tones, complemented by fresh and calm accents).
- Clean, professional design with plenty of white space.
- Accessible, warm, and inviting.

Functionalities:
- Online appointment scheduling or easy contact options.
- Blog/news section.
- Dedicated pages for therapists and therapies.
- Link to webshop.
- Possibility to expand the offer in the future (e.g., videos, downloads, or e-consultations).

What we would like to avoid:
- Pages that are too cluttered or confusing.
- Excessive text without clear structure.
- Stock photos lacking authenticity.

Target Audience:
People who consciously focus on their health, choose a natural approach, and are looking for a professional and reliable center where expertise and personal attention are central.

Additional Information:
The new website should bridge our 40-year history with the future. A place where visitors feel both familiar and inspired – and where they are immediately invited to get in touch, book an appointment, or visit our webshop.

You find our logo and impression in the uploads.

```html
<!DOCTYPE html>
<html lang="en">
<head>
<meta charset="utf-8">
<title>Brookvale Clinic for Herbal Care</title>
<link href="https://fonts.googleapis.com/css2?family=Montserrat:wght@400;500;700;800;900&family=Roboto:wght@400;500;700&display=swap" rel="stylesheet">
<style>
:root{
  --lime:#9cc91c;
  --lime-light:#c6e06a;
  --green-dark:#3b7314;
  --green-mid:#5e9a1e;
  --ink:#111111;
  --text:#555555;
  --muted:#8a8a8a;
  --white:#ffffff;
  --footer:#0a0a0a;
}
*{margin:0;padding:0;box-sizing:border-box}
html,body{width:1200px;height:5068px;overflow:hidden}
body{position:relative;background:var(--white);font-family:"Roboto",sans-serif;color:var(--text)}
.abs{position:absolute}
.btn{position:absolute;display:flex;align-items:center;justify-content:center;background:var(--lime);color:var(--white);font-family:"Montserrat",sans-serif;font-weight:700;border-radius:40px;box-shadow:3px 0 0 var(--lime-light);z-index:2}
.heading{position:absolute;left:0;width:1200px;text-align:center;font-family:"Montserrat",sans-serif;font-size:46px;color:var(--ink);letter-spacing:1px}
.heading b{font-weight:900}
.heading span{font-weight:400}
.photo{position:absolute}
/* header */
.logo-badge{position:absolute;left:146px;top:20px;width:200px;height:200px;border-radius:50%;background:var(--white);border:6px solid var(--lime);display:flex;align-items:center;justify-content:center;font-family:"Montserrat",sans-serif;font-weight:800;font-size:42px;color:var(--ink);z-index:3}
.call{left:680px;top:18px;display:flex;align-items:center;gap:14px}
.call .ic{width:28px;height:28px;border-radius:50%;background:var(--lime)}
.call small{display:block;font-size:14px;font-weight:700;color:var(--lime)}
.call strong{display:block;font-size:19px;color:var(--ink);font-weight:700}
.nav{left:446px;top:86px;display:flex;gap:26px;font-family:"Montserrat",sans-serif;font-weight:500;font-size:14px;color:var(--ink)}
/* hero */
.hero-bg{left:0;top:120px;width:1200px;height:720px;background:radial-gradient(circle at 78% 40%,#a6d36a 0%,#5f9c26 35%,#2f6a12 75%)}
.hero-title{position:absolute;left:142px;top:322px;font-family:"Montserrat",sans-serif;font-weight:500;font-size:46px;line-height:68px;color:var(--white);letter-spacing:1px;z-index:2}
.hero-tagline{position:absolute;left:146px;top:479px;font-size:18px;color:var(--white);z-index:2}
.dots{left:146px;top:655px;display:flex;gap:20px;z-index:2}
.dots i{width:11px;height:11px;border-radius:50%;background:var(--white)}
.dots i.on{background:var(--lime)}
/* about */
.about-text{left:610px;top:962px;width:442px;font-size:13.5px;line-height:29px;text-align:justify}
/* therapists */
.ther-bg{left:0;top:1377px;width:1200px;height:725px;background:linear-gradient(90deg,#f4f5f2,#eef0ec 60%,#e7e3dd)}
.card{position:absolute;background:var(--white);border-radius:12px;box-shadow:0 4px 14px rgba(0,0,0,.12)}
.card.active{box-shadow:4px 4px 0 var(--lime-light),0 4px 14px rgba(0,0,0,.12)}
.avatar{position:absolute;border-radius:50%;background:linear-gradient(135deg,#c9b8a4,#6b7c93)}
.card h3{position:absolute;font-family:"Montserrat",sans-serif;font-weight:500;font-size:20px;color:var(--ink)}
.card p{position:absolute;font-size:13.5px;line-height:22px;color:var(--text)}
.socials{position:absolute;display:flex;gap:6px}
.socials i{width:28px;height:28px;border-radius:50%;border:2px solid #444}
.arrow{position:absolute;width:44px;height:44px;border-radius:50%;border:2px solid #b9b9b9;display:flex;align-items:center;justify-content:center}
/* therapies */
.tcard{position:absolute;top:2313px;width:286px;height:289px;border-radius:10px;background:var(--white);border:1px solid #ddd;overflow:hidden}
.tcard .img{height:201px}
.tcard h4{position:absolute;left:20px;top:222px;font-family:"Montserrat",sans-serif;font-weight:800;font-size:16px;color:var(--ink)}
.tcard p{position:absolute;left:20px;top:251px;font-size:13px;color:var(--text)}
.tcard .go{position:absolute;right:20px;top:220px;width:26px;height:26px;border-radius:50%;background:var(--lime)}
.tcard.active{background:var(--lime);border-color:var(--lime)}
.tcard.active h4,.tcard.active p{color:var(--white)}
.tcard.active .go{background:var(--white)}
/* webshop */
.shop{position:absolute;top:3336px;width:434px;height:254px;background:var(--white);border-radius:8px}
.shop .img{position:absolute;left:12px;top:12px;width:203px;height:228px;border-radius:6px}
.shop h4{position:absolute;left:244px;top:40px;font-family:"Montserrat",sans-serif;font-weight:800;font-size:16px;color:var(--ink)}
.shop p{position:absolute;left:244px;top:70px;width:160px;font-size:15px;line-height:26px;color:var(--text)}
.stars{position:absolute;left:244px;top:130px;color:var(--lime);font-size:17px;letter-spacing:2px}
/* blog */
.post{position:absolute;top:3910px;width:295px}
.post .img{height:178px;position:relative}
.post .date{position:absolute;left:20px;bottom:0;background:#1a1a1a;color:var(--white);font-size:11px;font-weight:700;padding:7px 14px}
.post h4{margin-top:34px;font-family:"Montserrat",sans-serif;font-weight:700;font-size:14px;color:var(--ink)}
.post p{margin-top:12px;font-size:13px;line-height:22px;color:var(--muted)}
.post a{display:block;margin-top:10px;font-size:13px;font-weight:700;color:var(--lime);text-decoration:underline}
/* footer */
.footer{left:0;top:4620px;width:1200px;height:448px;background:var(--footer)}
.field{position:absolute;border:1px solid #bbb;background:var(--white);font-size:11px;color:#444;padding:8px 10px}
.foot-title{position:absolute;top:4642px;font-size:16px;font-weight:500;color:var(--white)}
.info{position:absolute;left:777px;display:flex;align-items:center;gap:20px;color:var(--white);font-size:15px;line-height:22px}
.info .ic{width:36px;height:36px;border-radius:50%;border:2px solid var(--white);flex:none}
.info .ic.fill{background:var(--lime);border-color:var(--lime)}
.foot-social{left:892px;top:4985px;display:flex;gap:8px}
.foot-social i{width:27px;height:27px;border-radius:50%;background:var(--white)}
.foot-social i.on{background:var(--lime)}
</style>
</head>
<body>

<!-- hero -->
<div class="abs hero-bg" role="img" aria-label="Green leaf dripping herbal oil into an amber bottle"></div>
<h1 class="hero-title">NATURAL CARE.<br>MODERN EXPERTISE.</h1>
<p class="hero-tagline">40 years of trusted naturopathic care in a calm, professional setting.</p>
<div class="btn" style="left:146px;top:541px;width:236px;height:50px;font-size:13px">BOOK AN APPOINTMENT</div>
<div class="abs dots"><i></i><i class="on"></i><i></i></div>
<svg class="abs" style="left:0;top:640px" width="1200" height="230" viewBox="0 0 1200 230">
  <path d="M0 120 C200 250 420 150 620 90 C820 30 1000 40 1200 150 L1200 230 L0 230Z" fill="var(--lime)"/>
  <path d="M0 150 C200 260 420 175 620 115 C820 55 1000 70 1200 175 L1200 230 L0 230Z" fill="var(--white)"/>
</svg>

<!-- header -->
<div class="logo-badge">BCHC</div>
<div class="abs call"><span class="ic"></span><div><small>CALL US</small><strong>0500 123 456</strong></div></div>
<div class="btn" style="left:862px;top:16px;width:190px;height:46px;font-size:12px">BOOK AN APPOINTMENT</div>
<nav class="abs nav"><span>HOME</span><span>ABOUT US</span><span>THERAPIES</span><span>THERAPISTS</span><span>BLOG</span><span>WEBSHOP</span><span>CONTACT</span></nav>

<!-- about -->
<div class="photo" style="left:0;top:850px;width:170px;height:570px;background:linear-gradient(160deg,#d8c9b2,#b8324a 45%,#5a3a2a)" role="img" aria-label="Bowls of herbal seeds and red spice powder"></div>
<svg class="abs" style="left:140px;top:950px" width="440" height="440" viewBox="0 0 440 440">
  <circle cx="220" cy="224" r="206" fill="none" stroke="var(--lime)" stroke-width="14"/>
  <circle cx="220" cy="224" r="178" fill="var(--lime-light)"/>
</svg>
<div class="photo" style="left:182px;top:996px;width:356px;height:356px;border-radius:50%;background:linear-gradient(135deg,#eef2ea,#b9c8b0)" role="img" aria-label="Smiling therapist in lab glasses holding a young plant"></div>
<div class="heading" style="left:610px;top:882px;width:auto;text-align:left"><b>ABOUT</b> <span>US</span></div>
<p class="abs about-text">Sed ut perspiciatis unde omnis iste natus error sit voluptatem accusantium doloremque laudantium, totam rem aperiam, eaque ipsa quae ab illo inventore veritatis et quasi architecto beatae vitae dicta sunt explicabo. Nemo enim ipsam voluptatem quia voluptas sit aspernatur aut odit aut fugit, sed quia consequuntur magni dolores eos qui ratione voluptatem sequi nesciunt. Neque porro quisquam est, qui dolorem ipsum quia dolor sit amet, consectetur, adipisci velit, sed quia non numquam eius modi tempora incidunt ut labore et dolore magnam aliquam quaerat voluptatem.</p>
<div class="btn" style="left:610px;top:1247px;width:147px;height:54px;font-size:14px">READ MORE</div>

<!-- therapists -->
<div class="abs ther-bg" role="img" aria-label="Soft faded photo of a therapist caring for a patient"></div>
<svg class="abs" style="left:0;top:1340px" width="1200" height="160" viewBox="0 0 1200 160">
  <path d="M0 60 C300 150 600 130 900 60 C1050 25 1130 20 1200 30 L1200 0 L0 0Z" fill="var(--white)"/>
  <path d="M0 60 C300 150 600 130 900 60 C1050 25 1130 20 1200 30" fill="none" stroke="#e4efc6" stroke-width="10"/>
</svg>
<div class="heading" style="top:1626px"><b>MEET OUR</b> <span>THERAPISTS</span></div>
<div class="arrow" style="left:80px;top:1860px"><svg width="14" height="14" viewBox="0 0 14 14"><path d="M9 2 L4 7 L9 12" fill="none" stroke="#b9b9b9" stroke-width="2"/></svg></div>
<div class="arrow" style="left:1076px;top:1860px"><svg width="14" height="14" viewBox="0 0 14 14"><path d="M5 2 L10 7 L5 12" fill="none" stroke="#b9b9b9" stroke-width="2"/></svg></div>
<div class="card active" style="left:222px;top:1750px;width:360px;height:260px">
  <h3 style="left:152px;top:40px">JOHN DOE</h3>
  <p style="left:152px;top:76px;width:185px">Sed ut perspiciatis unde omnis iste natus error sit voluptatem accusantium doloremque</p>
  <div class="socials" style="left:152px;top:186px"><i></i><i></i><i></i></div>
</div>
<div class="avatar" style="left:152px;top:1784px;width:196px;height:196px" role="img" aria-label="Portrait of therapist John Doe"></div>
<div class="card" style="left:688px;top:1750px;width:360px;height:260px">
  <h3 style="left:152px;top:40px">SMITHA DOE</h3>
  <p style="left:152px;top:76px;width:185px">Sed ut perspiciatis unde omnis iste natus error sit voluptatem accusantium doloremque</p>
  <div class="socials" style="left:152px;top:186px"><i></i><i></i><i></i></div>
</div>
<div class="avatar" style="left:618px;top:1784px;width:196px;height:196px" role="img" aria-label="Portrait of therapist Smitha Doe"></div>

<!-- therapies -->
<div class="photo" style="left:0;top:2160px;width:120px;height:640px;background:linear-gradient(160deg,#5f9a3a,#b98c63 55%,#e0c2aa)" role="img" aria-label="Palm leaves and a wooden bowl of herbal salt"></div>
<div class="photo" style="left:1050px;top:2620px;width:150px;height:340px;background:linear-gradient(160deg,#8cbf3c,#e48a2a 60%,#f3d0a0)" role="img" aria-label="Herbal capsules and a dried orange slice"></div>
<div class="heading" style="top:2204px"><b>FEATURED</b> <span>THERAPIES</span></div>
<div class="tcard" style="left:151px"><div class="img" style="background:linear-gradient(160deg,#4e8a2c,#8a5a2e)" role="img" aria-label="Herbs in a wooden bowl"></div><h4>HERBAL MEDICINE</h4><p>Sed ut perspiciatiomnis iste</p><span class="go"></span></div>
<div class="tcard active" style="left:456px"><div class="img" style="background:linear-gradient(160deg,#3f6e25,#a05a2a 60%,#e9e4d6)" role="img" aria-label="Homeopathy bottles with mortar and pestle"></div><h4>HOMEOPATHY</h4><p>Sed ut perspiciatiomnis iste</p><span class="go"></span></div>
<div class="tcard" style="left:761px"><div class="img" style="background:linear-gradient(160deg,#e9dcd2,#a8715a)" role="img" aria-label="Relaxing head massage treatment"></div><h4>MASSAGE THERAPHY</h4><p>Sed ut perspiciatiomnis iste</p><span class="go"></span></div>
<div class="arrow" style="left:1076px;top:2437px"><svg width="14" height="14" viewBox="0 0 14 14"><path d="M5 2 L10 7 L5 12" fill="none" stroke="#b9b9b9" stroke-width="2"/></svg></div>

<!-- webshop band -->
<svg class="abs" style="left:0;top:2900px" width="1200" height="800" viewBox="0 0 1200 800">
  <path d="M0 80 C300 170 650 150 900 90 C1050 55 1140 50 1200 60 L1200 800 L0 800Z" fill="var(--lime)"/>
  <path d="M0 40 C300 130 650 110 900 60 C1050 30 1140 25 1200 30" fill="none" stroke="#e4efc6" stroke-width="12"/>
</svg>
<div class="photo" style="left:150px;top:2689px;width:900px;height:444px;border-radius:14px;background:linear-gradient(135deg,#6d7d8e,#c9b6a4 45%,#8aa2c2)" role="img" aria-label="Video still of a smiling woman relaxing on a sofa"></div>
<svg class="abs" style="left:567px;top:2878px" width="66" height="66" viewBox="0 0 66 66"><circle cx="33" cy="33" r="31" fill="var(--white)" stroke="#222" stroke-width="3"/><path d="M26 20 L48 33 L26 46Z" fill="var(--lime)" stroke="#222" stroke-width="2"/></svg>
<div class="heading" style="top:3216px;color:var(--white)"><b>OUR</b> <span>WEBSHOP</span></div>
<div class="arrow" style="left:80px;top:3441px;border-color:#e2f0b8"><svg width="14" height="14" viewBox="0 0 14 14"><path d="M9 2 L4 7 L9 12" fill="none" stroke="#e2f0b8" stroke-width="2"/></svg></div>
<div class="arrow" style="left:1076px;top:3441px;border-color:#e2f0b8"><svg width="14" height="14" viewBox="0 0 14 14"><path d="M5 2 L10 7 L5 12" fill="none" stroke="#e2f0b8" stroke-width="2"/></svg></div>
<div class="shop" style="left:150px;box-shadow:4px 4px 0 var(--lime-light)"><div class="img" style="background:linear-gradient(160deg,#f1f1ee,#b78d60)" role="img" aria-label="Jars of herbal supplements with basil leaves"></div><h4>SUPPLEMENTS</h4><p>Sed ut perspiciatis unde omnis iste</p><div class="stars">★★★★★</div><div class="btn" style="left:244px;top:174px;width:118px;height:38px;font-size:11px">READ MORE</div></div>
<div class="shop" style="left:612px"><div class="img" style="background:linear-gradient(160deg,#f4f4f4,#9a5a22 50%,#e8e8e8)" role="img" aria-label="Amber bottle spilling natural remedy capsules"></div><h4>NATURAL REMEDIES</h4><p>Sed ut perspiciatis unde omnis iste</p><div class="stars">★★★★★</div><div class="btn" style="left:244px;top:174px;width:118px;height:38px;font-size:11px">READ MORE</div></div>

<!-- blog -->
<div class="heading" style="top:3806px"><b>BLOG</b> <span>POSTS</span></div>
<div class="post" style="left:144px"><div class="img" style="background:linear-gradient(135deg,#3a3a3a,#c39a7c)" role="img" aria-label="Therapist treating a patient's knee"><span class="date">22 MARCH,2025</span></div><h4>UM QUIA DOLOR SIT AMETONSECTE</h4><p>Sed ut perspiciatis unde omnis iste natus error sit voluptatem accusantium</p><a>READ MORE</a></div>
<div class="post" style="left:452px"><div class="img" style="background:linear-gradient(135deg,#d9dde0,#5a4a40)" role="img" aria-label="Consultation between two women"><span class="date" style="background:var(--lime)">22 MARCH,2025</span></div><h4>UM QUIA DOLOR SIT AMETONSECTE</h4><p>Sed ut perspiciatis unde omnis iste natus error sit voluptatem accusantium</p><a>READ MORE</a></div>
<div class="post" style="left:761px"><div class="img" style="background:linear-gradient(135deg,#eeeeea,#b8742a)" role="img" aria-label="Herbal tea being poured into a glass"><span class="date">22 MARCH,2025</span></div><h4>UM QUIA DOLOR SIT AMETONSECTE</h4><p>Sed ut perspiciatis unde omnis iste natus error sit voluptatem accusantium</p><a>READ MORE</a></div>
<div class="btn" style="left:498px;top:4288px;width:204px;height:52px;font-size:13px">VIEW MORE POSTS</div>
<div class="photo" style="left:960px;top:4250px;width:240px;height:180px;background:linear-gradient(160deg,#f2f2ef,#2f7a2a)" role="img" aria-label="Mortar with fresh herbs"></div>

<!-- footer -->
<div class="photo" style="left:0;top:4380px;width:500px;height:180px;background:linear-gradient(120deg,#1f4a3a,#8ab83a 55%,#e9a23a)" role="img" aria-label="Scattered spirulina tablets and herbal capsules"></div>
<svg class="abs" style="left:0;top:4380px" width="1200" height="260" viewBox="0 0 1200 260">
  <path d="M0 140 C200 210 420 200 600 150 C800 90 1000 60 1200 80 L1200 260 L0 260Z" fill="var(--lime)"/>
  <path d="M0 160 C200 230 420 220 600 170 C800 110 1000 80 1200 100 L1200 260 L0 260Z" fill="var(--white)"/>
  <path d="M0 180 C200 250 420 240 600 190 C800 130 1000 100 1200 120 L1200 260 L0 260Z" fill="var(--footer)"/>
</svg>
<div class="abs footer"></div>
<div class="logo-badge" style="left:522px;top:4407px;width:176px;height:176px;font-size:36px">BCHC</div>

<h5 class="foot-title" style="left:142px">Get In Touch:</h5>
<div class="field" style="left:144px;top:4685px;width:289px;height:32px">NAME :</div>
<div class="field" style="left:445px;top:4685px;width:287px;height:32px">PHONE :</div>
<div class="field" style="left:144px;top:4731px;width:588px;height:30px">EMAIL :</div>
<div class="field" style="left:144px;top:4774px;width:588px;height:71px">MESSAGE :</div>
<div class="btn" style="left:647px;top:4868px;width:85px;height:30px;font-size:11px;box-shadow:none">SUBMIT</div>

<h5 class="foot-title" style="left:777px">Contact Information</h5>
<div class="info" style="top:4686px"><span class="ic"></span><span>Willowbank Lane 12<br>8400 AB Brookvale</span></div>
<div class="info" style="top:4740px"><span class="ic fill"></span><span style="font-weight:700">500 123 456</span></div>
<div class="info" style="top:4790px"><span class="ic"></span><span>info@bchc-example.nl</span></div>
<div class="info" style="top:4842px"><span class="ic"></span><span style="font-weight:700">24/7 Service</span></div>

<div class="abs" style="left:136px;top:4943px;width:930px;height:1px;background:#333"></div>
<p class="abs" style="left:144px;top:4990px;font-size:13px;color:var(--white)">Copyrights © 2025, Companyname. All Rights Reserved. &nbsp;|&nbsp; Privacy policy &nbsp;|&nbsp; Terms of use</p>
<div class="abs foot-social"><i></i><i class="on"></i><i></i><i></i><i></i></div>

</body>
</html>
```